Plumbing business looking for a website update / to stand out

Looking to update the website with WordPress so looking for a WordPress template customised to our needs. The current website is http://www.corwinhaleplumbing.com.au/ and would like to keep the colour scheme of the green and grey. Like the idea of have menu across the top with drop down menus once mouse is over them.

Looking to stand out and look professional when compared to the competition
http://www.redgroveplumbing.net.au/
http://www.tovisplumbing.com.au/

```html
<!DOCTYPE html>
<html lang="en">
<head>
<meta charset="utf-8">
<title>Corwin Hale Plumbing</title>
<link href="https://fonts.googleapis.com/css2?family=Open+Sans:wght@400;600&display=swap" rel="stylesheet">
<style>
:root{
  --green:#7dc243;
  --nav-grey:#5f6266;
  --page-bg:#e8e8e6;
  --panel:#f7f7f7;
  --border:#d6d6d6;
  --text:#555;
  --heading:#3d3d3d;
  --footer:#3a3a3a;
  --footer-deep:#2a2a2a;
  --field:#262626;
  --white:#fff;
}
*{margin:0;padding:0;box-sizing:border-box}
html,body{width:1070px;height:1200px;overflow:hidden}
body{background:var(--page-bg);font-family:"Open Sans",Arial,sans-serif;color:var(--text);position:relative}
.top-stripe{position:absolute;left:0;top:0;width:1070px;height:7px;background:var(--green)}
.page{position:absolute;left:152px;top:7px;width:765px;height:1193px;background:var(--white)}
.abs{position:absolute}
/* header */
.brand-mark{left:50px;top:5px;width:50px;height:50px;border-radius:50%;background:var(--green)}
.brand-name{left:16px;top:60px;font-size:13px;font-weight:600;color:var(--heading);white-space:nowrap}
.brand-tag{left:16px;top:80px;font-size:6.5px;color:#999;white-space:nowrap}
.social-top{right:15px;top:12px;display:flex;gap:4px}
.social-top span{width:25px;height:25px;border-radius:50%;background:#5a5a5a}
.social-top span:first-child{background:var(--green)}
.search{left:612px;top:49px;width:138px;height:27px;border:1px solid var(--border);border-radius:3px;background:#fafafa;display:flex}
.search-btn{width:27px;height:25px;background:var(--green);border-radius:2px 0 0 2px;display:flex;align-items:center;justify-content:center}
.search-field{font-size:9px;color:#bbb;padding:7px 0 0 8px}
.nav{left:16px;top:87px;width:734px;height:36px;background:var(--nav-grey)}
.nav a{position:absolute;top:8px;font-size:14.5px;color:var(--white);text-decoration:none;white-space:nowrap}
.nav a.active{color:var(--green)}
/* slider */
.slider{left:16px;top:131px;width:734px;height:327px;background:linear-gradient(90deg,#8c8780 0%,#b4ada2 35%,#a8a6a3 60%,#c9ccce 80%,#9a9690 100%);box-shadow:0 6px 8px rgba(0,0,0,.25)}
.dots{left:18px;top:309px;display:flex;gap:5px}
.dots span{width:11px;height:11px;border-radius:50%;background:var(--white)}
.dots span:first-child{background:#ddd}
/* feature cards */
.card{top:508px;width:228px;height:137px;background:var(--panel);border:1px solid var(--border);border-top:2px solid var(--green);text-align:center}
.card-icon{position:absolute;left:89px;top:-22px;width:48px;height:48px;border-radius:50%;background:var(--green);display:flex;align-items:center;justify-content:center}
.card h2{margin-top:39px;font-size:21px;line-height:28px;font-weight:400;color:var(--green);letter-spacing:.5px}
.card p{margin:9px 14px 0;font-size:9.5px;line-height:11.5px;text-align:justify;text-align-last:center}
/* content */
.section-title{font-size:22px;line-height:30px;font-weight:400;color:var(--heading);letter-spacing:.5px}
.welcome{left:16px;top:728px;width:481px;height:205px;border:1px solid var(--border);background:var(--panel);padding:9px 13px;font-size:9.4px;line-height:11px;text-align:justify}
.welcome p{margin-bottom:11px}
.partner{left:521px;top:728px;width:229px;height:205px;border:1px solid var(--border);background:var(--panel);display:flex;align-items:center;justify-content:center}
.badge{width:130px;height:130px;border-radius:50%;border:6px solid var(--green);background:#eef5e6}
/* footer */
.footer{left:0;top:973px;width:765px;height:188px;background:var(--footer);color:var(--white)}
.footer h3{position:absolute;font-size:22px;line-height:30px;font-weight:400;color:var(--white);letter-spacing:.5px}
.menu{left:27px;top:39px;list-style:none;font-size:11.5px;line-height:17px}
.menu li::before{content:"";display:inline-block;width:5px;height:5px;border-radius:50%;background:var(--green);margin:0 12px 2px 0}
.menu li.active{color:var(--green)}
.detail{top:40px;font-size:11.5px;line-height:17px}
.detail .row{display:flex;align-items:center;gap:8px}
.detail .label{color:var(--green)}
.social-foot{top:146px;display:flex;gap:5px}
.social-foot span{width:25px;height:25px;border-radius:50%;background:#e6e6e6}
.social-foot span:first-child{background:var(--green)}
.field{background:var(--field);font-size:9.5px;color:#ccc;padding:0 7px;line-height:16px}
.send{left:521px;top:162px;width:65px;height:19px;background:var(--green);color:var(--white);font-size:11px;text-align:center;line-height:19px}
.copyright{left:0;top:1161px;width:765px;height:32px;background:var(--footer-deep);color:var(--white);font-size:9.5px;padding:10px 0 0 16px}
</style>
</head>
<body>
<div class="top-stripe"></div>
<div class="page">
  <header>
    <div class="abs brand-mark"></div>
    <div class="abs brand-name">Corwin Hale Plumbing</div>
    <div class="abs brand-tag">reliable plumbing for every project site</div>
    <div class="abs social-top"><span></span><span></span><span></span><span></span></div>
    <div class="abs search">
      <div class="search-btn"><svg width="14" height="14" viewBox="0 0 14 14"><circle cx="5.5" cy="5.5" r="4" fill="none" stroke="#fff" stroke-width="2"/><line x1="8.5" y1="8.5" x2="13" y2="13" stroke="#fff" stroke-width="2.4"/></svg></div>
      <div class="search-field">Search</div>
    </div>
    <nav class="abs nav">
      <a class="active" style="left:105px">Home</a>
      <a style="left:199px">Service</a>
      <a style="left:298px">Team</a>
      <a style="left:390px">Warrenty Agent</a>
      <a style="left:551px">Contact Us</a>
    </nav>
  </header>

  <div class="abs slider" role="img" aria-label="Photo of an installed gas hot water unit and pipework on a building wall">
    <div class="abs dots"><span></span><span></span><span></span><span></span></div>
  </div>

  <section class="abs card" style="left:16px">
    <div class="card-icon"><svg width="26" height="26" viewBox="0 0 26 26"><circle cx="10" cy="15" r="5" fill="none" stroke="#fff" stroke-width="3" stroke-dasharray="2.5 1.5"/><circle cx="18" cy="8" r="3.5" fill="none" stroke="#fff" stroke-width="2.5" stroke-dasharray="2 1.3"/></svg></div>
    <h2>OUR SERVICES</h2>
    <p>Lorem Ipsum is simply dummy text of the printing and typesetting industry. Lorem Ipsum has been the industry's standard dummy text ever since the 1500</p>
  </section>
  <section class="abs card" style="left:269px">
    <div class="card-icon"><svg width="26" height="26" viewBox="0 0 26 26" fill="#fff"><circle cx="10" cy="8" r="4"/><circle cx="17" cy="9" r="3.5"/><path d="M3 21c0-5 3-8 7-8s7 3 7 8z"/><path d="M14 14c3-1 8 1 9 7h-5c0-3-2-5-4-7z"/></svg></div>
    <h2>OUR TEAM</h2>
    <p>Lorem Ipsum is simply dummy text of the printing and typesetting industry. Lorem Ipsum has been the industry's standard dummy text ever since the 1500</p>
  </section>
  <section class="abs card" style="left:521px">
    <div class="card-icon"><svg width="24" height="24" viewBox="0 0 24 24"><path d="M6 3l4 4-2 3c1 3 3 5 6 6l3-2 4 4-3 4C10 21 3 14 2 6z" fill="none" stroke="#fff" stroke-width="2" stroke-linejoin="round"/></svg></div>
    <h2>JOIN US</h2>
    <p>Lorem Ipsum is simply dummy text of the printing and typesetting industry. Lorem Ipsum has been the industry's standard dummy text ever since the 1500</p>
  </section>

  <h2 class="abs section-title" style="left:16px;top:684px">Welcome to chp</h2>
  <h2 class="abs section-title" style="left:521px;top:684px">Partner Logo</h2>

  <div class="abs welcome">
    <p>Corwin Hale Plumbing Pty Ltd was established in 1986 and is known for high quality service that employs 5 qualified plumbing tradesmen, a Carpenter and a Sub Contractor working primarily in the Commercial and Industrial Sectors of Plumbing and Maintenance.</p>
    <p>As a locally owned Western Australian Industrial /Commercial/Maintenance Plumbing Company, we are committed to providing the best practice that will keep us as a leader in the competitive and challenging market of providing unique customer service to our clientele base.</p>
    <p>Committed to training we currently have 2 apprentice learning the trade under our direction to ensure our clientele have only the most up to date skills and techniques made available to each task at hand.</p>
    <p>We are members of The Trade Plumbers Guild and ensure work is carried out under the regulations of the 'Plumbers Licensing Board' using the Australian Standard AS3500 bylaws, contractors license number PL 4471.</p>
    <p>Thank you for visiting our website please check out each division for a more specific understanding of our services.</p>
  </div>
  <div class="abs partner"><div class="badge" role="img" aria-label="Partner association badge"></div></div>

  <footer class="abs footer">
    <h3 style="left:16px;top:5px">Main Menu</h3>
    <ul class="abs menu">
      <li class="active">Home</li><li>Service</li><li>Team</li><li>Warrenty Agent</li><li>Contact</li>
    </ul>
    <h3 style="left:238px;top:5px">Personal Detail</h3>
    <div class="abs detail" style="left:242px">
      <div class="row"><svg width="14" height="14" viewBox="0 0 24 24"><path d="M6 3l4 4-2 3c1 3 3 5 6 6l3-2 4 4-3 4C10 21 3 14 2 6z" fill="#fff"/></svg><span><span class="label">Phone No:</span> 0400 555 182</span></div>
      <div class="row"><svg width="14" height="14" viewBox="0 0 24 24"><path d="M12 2a7 7 0 0 0-7 7c0 5 7 13 7 13s7-8 7-13a7 7 0 0 0-7-7z" fill="#fff"/><circle cx="12" cy="9" r="2.5" fill="#3a3a3a"/></svg><span><span class="label">Address :</span> PO Box 4821</span></div>
      <div style="padding-left:22px">Harlow Bay WA 6999</div>
    </div>
    <h3 style="left:238px;top:105px">Social Links</h3>
    <div class="abs social-foot" style="left:242px"><span></span><span></span><span></span><span></span></div>
    <h3 style="left:521px;top:5px">Contact</h3>
    <div class="abs field" style="left:521px;top:44px;width:109px;height:18px;border:1px solid var(--green)">Name</div>
    <div class="abs field" style="left:641px;top:44px;width:109px;height:18px;line-height:18px">Email</div>
    <div class="abs field" style="left:521px;top:68px;width:229px;height:86px;padding-top:4px;line-height:12px">Message</div>
    <div class="abs send">Send</div>
  </footer>
  <div class="abs copyright">Copyright © 2014 - All right reserved</div>
</div>
</body>
</html>
```